Welcome Card Banner Desing for email suscriptors

to get involved on this task please check my site tulavendo.app
I wish for this task a welcome postal card to get subscribers for the newsletter and get a Coupon Code for discounts,
Keep in mind Velisso is a platform where customers (girls) can get any fashion high-end accessories ready to wear, to see the categories please visit our shop.

Target Market(s)

World wide people between 18-60 years old

Industry/Entity Type

Fashion

Coding

Coded - Design and coding required

Number of Pages Required

1 page

Font styles to use
Sans Serif

Colors
a64599
ffffff
ffc214
faa54b

Requirements
Must have
• Simplicity
• to get involved on this task please check my site tulavendo.app
• I wish for this task a welcome postal card to get subscribers for the newsletter and get a Coupon Code for discounts,
• Keep in mind Velisso is a platform where customers (girls) can get any fashion high-end accessories ready to wear, to see the categories please visit our shop.
Nice to have
• Field for customer fill an email or just skip the banner
Should not have
• Bad grammar

```html
<!DOCTYPE html>
<html lang="en">
<head>
<meta charset="UTF-8">
<title>Velisso – Welcome Card</title>
<link rel="stylesheet" href="https://fonts.googleapis.com/css2?family=Arimo:wght@400;700&display=swap">
<style>
  :root {
    --stage-bg: #3f3f3f;
    --card-frame: #f1efed;
    --white: #ffffff;
    --ink: #2a2a2a;
    --discount-tone: #c0702a;
    --subscribe-bar: rgba(255, 255, 255, 0.82);
    --hero-light: #c9c1b7;
    --hero-warm: #b9652f;
    --hero-deep: #5b4335;
    --paper-light: #dcae72;
    --paper-mid: #c9955a;
    --paper-dark: #a9723f;
  }
  * { box-sizing: border-box; margin: 0; padding: 0; }
  html, body {
    width: 1200px;
    height: 580px;
    overflow: hidden;
  }
  body {
    background: var(--stage-bg);
    font-family: "Arimo", Arial, sans-serif;
    position: relative;
  }
  .welcome-card {
    position: absolute;
    left: 45px;
    top: 7px;
    width: 1110px;
    height: 566px;
    background: var(--card-frame);
  }
  .hero {
    position: absolute;
    left: 28px;
    top: 23px;
    width: 701px;
    height: 524px;
    overflow: hidden;
  }
  .hero-photo {
    position: absolute;
    inset: 0;
    background: linear-gradient(160deg, var(--hero-light) 0%, var(--hero-warm) 55%, var(--hero-deep) 100%);
  }
  .hero-title {
    position: absolute;
    left: 0;
    top: 64px;
    width: 100%;
    text-align: center;
    color: var(--white);
    font-size: 58px;
    font-weight: 700;
    line-height: 65px;
    text-shadow: 2px 3px 4px rgba(0, 0, 0, 0.55);
  }
  .subscribe-bar {
    position: absolute;
    left: 24px;
    top: 361px;
    width: 654px;
    height: 53px;
    background: var(--subscribe-bar);
    color: var(--ink);
    font-size: 27px;
    font-weight: 700;
    display: flex;
    align-items: center;
    justify-content: center;
  }
  .coupon {
    position: absolute;
    left: 729px;
    top: 23px;
    width: 350px;
    height: 524px;
    overflow: hidden;
  }
  .coupon-paper {
    position: absolute;
    inset: 0;
    background: radial-gradient(ellipse 70% 60% at 50% 40%, var(--paper-light) 0%, var(--paper-mid) 60%, var(--paper-dark) 100%);
  }
  .coupon-content {
    position: absolute;
    inset: 0;
    text-align: center;
  }
  .coupon-heading {
    position: absolute;
    left: 0;
    top: 86px;
    width: 100%;
    font-size: 57px;
    font-weight: 400;
    line-height: 1;
    color: var(--discount-tone);
  }
  .coupon-offer {
    position: absolute;
    left: 0;
    top: 150px;
    width: 100%;
    font-size: 38px;
    line-height: 1;
    color: var(--ink);
  }
  .coupon-button {
    position: absolute;
    left: 54px;
    top: 262px;
    width: 242px;
    height: 37px;
    border: 1.5px dashed var(--ink);
    display: flex;
    align-items: center;
    justify-content: center;
    font-size: 18px;
    font-weight: 700;
    color: var(--ink);
  }
  .brand-name {
    position: absolute;
    left: 0;
    top: 456px;
    width: 100%;
    font-size: 17px;
    font-weight: 700;
    color: var(--ink);
  }
  .brand-copyright {
    position: absolute;
    left: 0;
    top: 484px;
    width: 100%;
    font-size: 8px;
    color: var(--ink);
  }
  .ticket-notch {
    position: absolute;
    width: 15px;
    height: 15px;
    border-radius: 50%;
    background: var(--card-frame);
    left: 897px;
  }
  .ticket-notch--top { top: 16px; }
  .ticket-notch--bottom { top: 540px; }
</style>
</head>
<body>
  <main class="welcome-card">
    <section class="hero">
      <div class="hero-photo" role="img" aria-label="Fashion photo: a hand holding an orange leather handbag beside legs in jeans and red glitter heels"></div>
      <h1 class="hero-title">"Welcome<br>to the finest<br>shop"</h1>
      <div class="subscribe-bar">Subscribe</div>
    </section>

    <aside class="coupon">
      <div class="coupon-paper" role="img" aria-label="Aged brown paper texture"></div>
      <div class="coupon-content">
        <h2 class="coupon-heading">Discount</h2>
        <p class="coupon-offer">Upto 30%</p>
        <div class="coupon-button">get coupon code</div>
        <p class="brand-name">Velisso</p>
        <p class="brand-copyright">©Copyright 2019, Velisso</p>
      </div>
    </aside>

    <span class="ticket-notch ticket-notch--top"></span>
    <span class="ticket-notch ticket-notch--bottom"></span>
  </main>
</body>
</html>
```